Harbor Nightclub

Nightclub flyer., digital single sided, for KV and PX. I included samples of some previous flyers we've used. Sample Info:
HARBOR
FRIDAYS
FRI MAY 1 2020
DJ VORTAN (club floor)
DJ RUZO & DJ TAV (residents on the lounge floor)
4217 Marlow Avenue Sacramento
www.harborvenuehall.example for list/VIP inquiries

Target Market(s)

Upscale top 40 crowd but want some cool and artsy like the examples included.

Font styles to use
Sans Serif

Requirements
Must have
• Harbor Logo
Nice to have
• Would be nice if the flyer can be incorporated later with DJ photos (sometimes we will add dj photos to pixagram etc). Would like a big city type of feel.
Should not have
• Nothing too sexual.

```html
<!DOCTYPE html>
<html lang="en">
<head>
<meta charset="utf-8">
<title>Harbor Nightclub — Friday May 1</title>
<link rel="stylesheet" href="https://fonts.googleapis.com/css2?family=Jost:wght@300;400;700&display=swap">
<style>
  :root {
    --sky-top: #2c1a93;
    --sky-mid: #3a1f9e;
    --sky-low: #4a1e92;
    --sky-base: #561c86;
    --city-deep: #281c7c;
    --city-blue: #3f2cb4;
    --city-violet: #7a45dc;
    --city-magenta: #c23ad0;
    --city-pink: #d44fd8;
    --ink: #ffffff;
    --mark: #ead6f2;
  }
  * { margin: 0; padding: 0; box-sizing: border-box; }
  html, body { width: 960px; height: 1200px; overflow: hidden; background: var(--sky-top); }
  .flyer {
    position: relative;
    width: 960px;
    height: 1200px;
    overflow: hidden;
    background:
      radial-gradient(ellipse 520px 300px at 700px 1000px, rgba(120, 30, 140, 0.45), rgba(120, 30, 140, 0) 70%),
      radial-gradient(ellipse 600px 400px at 760px 250px, rgba(70, 50, 190, 0.35), rgba(70, 50, 190, 0) 70%),
      linear-gradient(180deg, var(--sky-top) 0%, var(--sky-mid) 45%, var(--sky-low) 75%, var(--sky-base) 100%);
    font-family: "Jost", "Helvetica Neue", Arial, sans-serif;
    color: var(--ink);
  }
  .city-art {
    position: absolute;
    left: 0; top: 0;
    width: 520px; height: 1200px;
    background:
      radial-gradient(ellipse 200px 260px at 270px 520px, rgba(150, 110, 240, 0.55), rgba(150, 110, 240, 0) 70%),
      radial-gradient(ellipse 300px 220px at 160px 880px, rgba(225, 80, 220, 0.75), rgba(225, 80, 220, 0) 72%),
      radial-gradient(ellipse 260px 180px at 120px 1100px, rgba(180, 60, 200, 0.6), rgba(180, 60, 200, 0) 70%),
      linear-gradient(180deg, var(--city-deep) 0%, var(--city-blue) 28%, var(--city-violet) 55%, var(--city-magenta) 75%, #8a34c0 100%);
    -webkit-mask-image: linear-gradient(90deg, #000 0%, #000 55%, rgba(0,0,0,0.5) 75%, transparent 100%);
    mask-image: linear-gradient(90deg, #000 0%, #000 55%, rgba(0,0,0,0.5) 75%, transparent 100%);
    opacity: 0.85;
  }
  .address {
    position: absolute;
    top: 40px; left: 0; width: 100%;
    text-align: center;
    font-weight: 300;
    font-size: 27px;
    letter-spacing: 0.28em;
    text-indent: 0.28em;
  }
  .headliner {
    position: absolute;
    top: 418px; left: 0; width: 100%;
    text-align: center;
    font-weight: 400;
    font-size: 130px;
    line-height: 1;
  }
  .residents {
    position: absolute;
    top: 578px; left: 0; width: 100%;
    text-align: center;
    font-weight: 400;
    font-size: 81px;
    line-height: 1;
  }
  .footer-line {
    position: absolute;
    top: 1070px; left: 61px;
    display: flex;
    align-items: center;
    height: 80px;
  }
  .date {
    font-weight: 700;
    font-size: 46px;
    letter-spacing: 0.26em;
  }
  .divider { width: 13px; height: 13px; margin: 0 30px 0 6px; }
  .brand { display: flex; align-items: center; gap: 16px; }
  .brand-dot { width: 72px; height: 72px; border-radius: 50%; background: var(--mark); }
  .brand-name {
    font-weight: 400;
    font-size: 38px;
    letter-spacing: 0.03em;
    color: var(--mark);
  }
  .website {
    position: absolute;
    top: 1150px; left: 0; width: 100%;
    text-align: center;
    font-weight: 300;
    font-size: 29px;
    letter-spacing: 0.01em;
  }
</style>
</head>
<body>
  <main class="flyer">
    <div class="city-art" role="img" aria-label="Upward view of glowing skyscraper grid against a starry violet night sky"></div>

    <p class="address">4217 MARLOW AVENUE SACRAMENTO</p>

    <h1 class="headliner">DJ VORTAN</h1>
    <h2 class="residents">DJ RUZO &amp; DJ TAV</h2>

    <div class="footer-line">
      <span class="date">FRIDAY MAY 1</span>
      <svg class="divider" viewBox="0 0 14 14" aria-hidden="true">
        <polygon points="7,0 14,7 7,14 0,7" fill="#ffffff"/>
      </svg>
      <div class="brand">
        <span class="brand-dot" aria-hidden="true"></span>
        <span class="brand-name">HARBOR</span>
      </div>
    </div>

    <p class="website">WWW.HARBORVENUEHALL.EXAMPLE</p>
  </main>
</body>
</html>
```